Business Card Design Project

I need a business card design for an Organic drive thru coffee kiosk. We will serve organic coffee, teas & smoothies and will serve healthy breakfast food/snacks for people on the go.
I want the card to have 2-3 colors max (earthy colors like browns, greens and so on).
I have attached the logo I want used and would love to play off the theme of "balance."
Include:
Tidy-Kettle Coffee
address: 4820 Gorvin Ct. Larkton, KS 27583
phone: 555-731-4062
website: www.tidy-kettle.com (website is not up yet but still include it on card)
email: Rosalind@tidy-kettle.com
I want one of the following sayings somewhere on the card (the front or back is fine):
"Sip & Savor Well, on the go!"
"Break the fast with Tidy-Kettle"
Maybe on the back list what we offer:
-Organic coffee, espresso & tea
-Blendora smoothies & protein shakes
-Zesty Pour (100% fresh local fruit and veggies)
-Tender Nibs

```html
<!DOCTYPE html>
<html lang="en">
<head>
<meta charset="utf-8">
<title>Tidy-Kettle Coffee – Business Card</title>
<link rel="stylesheet" href="https://fonts.googleapis.com/css2?family=Questrial&display=swap">
<style>
  :root {
    --leaf: #5b8a27;
    --leaf-light: #679a31;
    --leaf-dark: #456e1c;
    --sky: #48ade2;
    --sky-light: #86cbee;
    --cream: #e6e4bf;
    --bean: #5a2a1a;
    --paper: #ececec;
    --white: #ffffff;
  }
  * { margin: 0; padding: 0; box-sizing: border-box; }
  html, body { width: 1200px; height: 838px; overflow: hidden; }
  body {
    background: var(--paper);
    font-family: "Questrial", "Century Gothic", sans-serif;
    position: relative;
  }
  .card {
    position: absolute;
    left: 285px;
    width: 630px;
    height: 360px;
    overflow: hidden;
    box-shadow: 0 10px 24px rgba(0,0,0,0.22);
  }
  .card--back { top: 38px; }
  .card--front { top: 438px; }
  .card__art { position: absolute; inset: 0; width: 100%; height: 100%; }

  .brand {
    position: absolute;
    display: flex;
    align-items: center;
    gap: 10px;
    font-size: 34px;
    line-height: 1;
  }
  .brand__dot {
    width: 30px; height: 30px;
    border-radius: 50%;
    background: currentColor;
  }
  .card--front .brand { right: 34px; top: 92px; color: var(--bean); }
  .card--back .brand { right: 34px; bottom: 46px; color: var(--cream); font-size: 28px; }
  .card--back .brand__dot { width: 24px; height: 24px; }

  .contact {
    position: absolute;
    left: 52px;
    top: 178px;
    list-style: none;
    color: var(--cream);
    font-size: 18px;
  }
  .contact__item {
    display: flex;
    align-items: center;
    gap: 14px;
    height: 29px;
  }
  .contact__icon { width: 20px; height: 20px; flex: none; fill: var(--cream); }
  .contact__icon--blank { visibility: hidden; }

  .offer {
    position: absolute;
    left: 40px;
    top: 30px;
    color: var(--white);
  }
  .offer__list {
    list-style: none;
    font-size: 13px;
    line-height: 1.45;
    margin-bottom: 14px;
  }
  .offer__saying {
    font-size: 28px;
    line-height: 1.25;
    white-space: nowrap;
  }
</style>
</head>
<body>

<section class="card card--back" aria-label="Card back">
  <svg class="card__art" viewBox="0 0 630 360" preserveAspectRatio="none" aria-hidden="true">
    <defs>
      <radialGradient id="skyGlowBack" cx="0.35" cy="0.45" r="0.7">
        <stop offset="0" stop-color="var(--sky-light)"/>
        <stop offset="1" stop-color="var(--sky)"/>
      </radialGradient>
    </defs>
    <rect width="630" height="360" fill="var(--leaf)"/>
    <circle cx="600" cy="330" r="260" fill="var(--leaf-light)" opacity="0.5"/>
    <path d="M0 0 H560 C600 80 560 170 470 215 C360 270 220 290 0 300 Z" fill="var(--leaf-dark)"/>
    <path d="M0 0 H520 C555 70 520 150 440 190 C340 240 210 258 0 262 Z" fill="url(#skyGlowBack)"/>
  </svg>
  <div class="offer">
    <ul class="offer__list">
      <li>Tender Nibs</li>
      <li>Organic coffee, espresso &amp; tea</li>
      <li>Blendora smoothies &amp; protein shakes</li>
      <li>Zesty Pour (100% fresh local fruit and veggies)</li>
    </ul>
    <p class="offer__saying">"Sip &amp; Savor Well, on the go!"</p>
    <p class="offer__saying">"Break the fast with Tidy-Kettle"</p>
  </div>
  <div class="brand"><span class="brand__dot"></span><span class="brand__name">Tidy-Kettle</span></div>
</section>

<section class="card card--front" aria-label="Card front">
  <svg class="card__art" viewBox="0 0 630 360" preserveAspectRatio="none" aria-hidden="true">
    <defs>
      <radialGradient id="skyGlowFront" cx="0.55" cy="0.35" r="0.6">
        <stop offset="0" stop-color="var(--sky-light)"/>
        <stop offset="1" stop-color="var(--sky)"/>
      </radialGradient>
    </defs>
    <rect width="630" height="360" fill="var(--leaf)"/>
    <circle cx="120" cy="320" r="250" fill="var(--leaf-light)" opacity="0.5"/>
    <path d="M90 0 H630 V270 C520 280 400 240 300 160 C220 95 160 40 90 0 Z" fill="var(--leaf-dark)"/>
    <path d="M160 0 H630 V228 C520 236 410 200 320 130 C260 82 210 30 160 0 Z" fill="url(#skyGlowFront)"/>
  </svg>
  <div class="brand"><span class="brand__dot"></span><span class="brand__name">Tidy-Kettle</span></div>
  <ul class="contact">
    <li class="contact__item">
      <svg class="contact__icon" viewBox="0 0 20 20" aria-hidden="true"><path d="M10 2 L19 10 H16 V18 H12 V13 H8 V18 H4 V10 H1 Z"/></svg>
      <span>Tidy-Kettle Coffee</span>
    </li>
    <li class="contact__item">
      <svg class="contact__icon contact__icon--blank" viewBox="0 0 20 20" aria-hidden="true"></svg>
      <span>4820 Gorvin Ct. Larkton, KS 27583</span>
    </li>
    <li class="contact__item">
      <svg class="contact__icon" viewBox="0 0 20 20" aria-hidden="true"><path d="M3 5 C3 3 5 2 10 2 C15 2 17 3 17 5 V7 H13 V5 H7 V7 H3 Z"/><rect x="3" y="9" width="14" height="9" rx="2"/></svg>
      <span>555-731-4062</span>
    </li>
    <li class="contact__item">
      <svg class="contact__icon" viewBox="0 0 20 20" aria-hidden="true"><circle cx="10" cy="10" r="9"/><path d="M1 10 H19 M10 1 V19" stroke="var(--leaf)" stroke-width="1.5"/></svg>
      <span>www.tidy-kettle.com</span>
    </li>
    <li class="contact__item">
      <svg class="contact__icon" viewBox="0 0 20 20" aria-hidden="true"><rect x="1" y="4" width="18" height="12"/><path d="M1 4 L10 11 L19 4" fill="none" stroke="var(--leaf)" stroke-width="1.5"/></svg>
      <span>Rosalind@tidy-kettle.com</span>
    </li>
  </ul>
</section>

</body>
</html>
```